Business card design for new eCommerce site focusing on integrity and strong businsess tactics

We need a business card that will stand out and be memorable. Something with color that matches our company logo colors. Think high end version of Tallyhop. There are 2 logos provided. The parent company is called Brightwell Craft Partners and we are presenting a new and very exciting eCommerce site called KestrelTradeHub.example.

Target Market(s)

Our target markets are in the Activities, Food and Beverage, Health and Beauty

Industry/Entity Type

Marketing

Contact Information for Business Card

We have 4 members that need cards...I will provide all info to the winner of the design contest
Business Address is
47390 West 63rd Lane, Suite K204
Phoenix AZ 85061

Font styles to use
Serif
Sans Serif

Colors

Designer to choose colors to be used in the design.

Requirements
Must have
• The card must be memorable...should be unique in design but must exude integrity and be playful .
• I have provided several colors or our parent company...please feel free to use which ever
Nice to have
• I will leave this up to you. Feel free to use other images of your choosing that wraps around our client.....Activities, Dining, Health, Beauty
Should not have
• just dont be boring

```html
<!DOCTYPE html>
<html lang="en">
<head>
<meta charset="utf-8">
<title>KestrelTradeHub.example – Business Card</title>
<link rel="stylesheet" href="https://fonts.googleapis.com/css2?family=Questrial&family=Open+Sans:wght@400;700&display=swap">
<style>
  :root {
    --bg: #e6e7ea;
    --navy: #1b2554;
    --navy-light: #26346e;
    --green: #7cc242;
    --blue: #2f86c1;
    --ink: #1a2148;
    --grey: #6b6e76;
    --white: #ffffff;
  }
  * { margin: 0; padding: 0; box-sizing: border-box; }
  html, body { width: 1200px; height: 1000px; overflow: hidden; background: var(--bg); }
  body { position: relative; font-family: "Open Sans", Arial, sans-serif; }

  .card {
    position: absolute;
    left: 270px;
    width: 660px;
    height: 378px;
    border-radius: 22px;
    overflow: hidden;
    box-shadow: 0 6px 18px rgba(0,0,0,0.18);
  }

  /* Front */
  .card--front {
    top: 108px;
    background: linear-gradient(120deg, var(--navy) 0%, var(--navy-light) 45%, var(--navy) 100%);
  }
  .brand {
    position: absolute;
    display: flex;
    flex-direction: column;
  }
  .brand__row { display: flex; align-items: center; gap: 12px; }
  .brand__dot { border-radius: 50%; background: var(--green); flex: none; }
  .brand__name { font-family: "Questrial", Arial, sans-serif; color: var(--green); white-space: nowrap; }
  .brand__tagline { font-family: "Questrial", Arial, sans-serif; letter-spacing: 2px; white-space: nowrap; }

  .card--front .brand { left: 118px; top: 160px; }
  .card--front .brand__dot { width: 34px; height: 34px; }
  .card--front .brand__name { font-size: 29px; }
  .card--front .brand__tagline { font-size: 16px; color: var(--white); margin: 6px 0 0 46px; }

  .card--front .site {
    position: absolute; left: 0; right: 0; bottom: 26px;
    text-align: center; color: var(--white); font-size: 15px;
  }

  /* Back */
  .card--back { top: 521px; background: var(--white); }
  .card--back .brand { left: 32px; top: 64px; }
  .card--back .brand__dot { width: 30px; height: 30px; }
  .card--back .brand__name { font-size: 25px; }
  .card--back .brand__tagline { font-size: 14px; color: var(--grey); margin: 6px 0 0 42px; }

  .contact { position: absolute; left: 30px; top: 181px; color: var(--grey); font-size: 14.5px; }
  .contact__name { color: var(--green); font-weight: 700; font-size: 19px; line-height: 1.2; }
  .contact__role { margin-bottom: 13px; }
  .contact__address { line-height: 1.45; margin-bottom: 13px; }
  .contact__line { display: flex; align-items: center; gap: 6px; line-height: 1.65; }
  .contact__icon { width: 16px; height: 16px; flex: none; }

  .partner {
    position: absolute; right: 48px; top: 250px; width: 160px;
    display: flex; flex-direction: column; align-items: center; gap: 10px;
  }
  .partner__dot { width: 40px; height: 40px; border-radius: 50%; background: var(--ink); }
  .partner__name {
    color: var(--ink); font-weight: 700; font-size: 16px; text-align: center; line-height: 1.2;
  }

  .footer-bands { position: absolute; left: 0; bottom: 0; width: 660px; height: 40px; }
  .footer-site {
    position: absolute; right: 18px; bottom: 7px; color: var(--white); font-size: 14.5px;
  }
</style>
</head>
<body>

  <section class="card card--front" aria-label="Card front">
    <div class="brand">
      <div class="brand__row">
        <span class="brand__dot"></span>
        <span class="brand__name">KestrelTradeHub.example</span>
      </div>
      <span class="brand__tagline">Activities-Dining-Health-Beauty</span>
    </div>
    <p class="site">www.KestrelTradeHub.example</p>
  </section>

  <section class="card card--back" aria-label="Card back">
    <div class="brand">
      <div class="brand__row">
        <span class="brand__dot"></span>
        <span class="brand__name">KestrelTradeHub.example</span>
      </div>
      <span class="brand__tagline">Activities-Dining-Health-Beauty</span>
    </div>

    <div class="contact">
      <p class="contact__name">Owen Hartley</p>
      <p class="contact__role">Managing Director</p>
      <p class="contact__address">47390 West 63rd Lane, Suite K204<br>Phoenix AZ 85061</p>
      <p class="contact__line">
        <svg class="contact__icon" viewBox="0 0 16 16" aria-hidden="true">
          <circle cx="8" cy="8" r="7" fill="none" stroke="#2f86c1" stroke-width="1.3"/>
          <path d="M5.4 4.6l1.3-.4.8 1.8-.9.7c.4.9 1 1.6 1.9 2l.7-.9 1.8.8-.4 1.3c-2.6.2-5.4-2.6-5.2-5.3z" fill="#2f86c1"/>
        </svg>
        +61 425 318 904
      </p>
      <p class="contact__line">
        <svg class="contact__icon" viewBox="0 0 16 16" aria-hidden="true">
          <circle cx="8" cy="8" r="7" fill="none" stroke="#2f86c1" stroke-width="1.3"/>
          <rect x="4.3" y="5.4" width="7.4" height="5.2" fill="#2f86c1"/>
          <path d="M4.5 5.6L8 8.4l3.5-2.8" fill="none" stroke="#fff" stroke-width="0.9"/>
        </svg>
        info@KestrelTradeHub.example
      </p>
    </div>

    <div class="partner">
      <span class="partner__dot"></span>
      <span class="partner__name">Brightwell Craft Partners</span>
    </div>

    <svg class="footer-bands" viewBox="0 0 660 40" preserveAspectRatio="none" aria-hidden="true">
      <path d="M0 22 H395 L388 26 H0 Z" fill="var(--green)"/>
      <path d="M0 28 H380 C392 28 398 12 414 12 H660 V40 H0 Z" fill="var(--blue)"/>
    </svg>
    <p class="footer-site">www.KestrelTradeHub.example</p>
  </section>

</body>
</html>
```